Copper Lantern Gin

The gin is 100% proof and men and anbody 18 - 30 year old will be a target market - the bottle is very distinctive and lends itself to a square label.

The bottle is curved with a large front face that lends itself to a striking design. There should be enough space around the label to show the black gin in the bottle as this is a feature.

The current bottle with the existing label is attached below as is the new glass bottle. The new gin will be coloured black.

Font styles to use
Decorative
Script

```html
<!DOCTYPE html>
<html lang="en">
<head>
<meta charset="utf-8">
<title>Copper Lantern Gin — Navy Strength Label</title>
<link rel="stylesheet" href="https://fonts.googleapis.com/css2?family=Bodoni+Moda:wght@400;500&display=swap">
<style>
  :root {
    --label-black: #000000;
    --silver-light: #ffffff;
    --silver-mid: #a8a8a8;
    --silver-dark: #6e6e6e;
    --crimson: #8c0a1e;
    --crimson-deep: #3d0009;
  }
  html, body {
    margin: 0;
    padding: 0;
    width: 1200px;
    height: 1000px;
    overflow: hidden;
    background: var(--label-black);
  }
  .label {
    display: block;
    width: 1200px;
    height: 1000px;
  }
  .label-type {
    font-family: "Bodoni Moda", "Didot", serif;
    font-weight: 400;
  }
</style>
</head>
<body>
<svg class="label" viewBox="0 0 1200 1000" xmlns="http://www.w3.org/2000/svg" aria-labelledby="label-title">
  <title id="label-title">Copper Lantern Navy Strength British Gin, 50cl, 57% ABV</title>
  <defs>
    <linearGradient id="silver" x1="0" y1="0" x2="1" y2="0.15">
      <stop offset="0" stop-color="var(--silver-mid)"/>
      <stop offset="0.2" stop-color="var(--silver-light)"/>
      <stop offset="0.35" stop-color="var(--silver-dark)"/>
      <stop offset="0.5" stop-color="var(--silver-light)"/>
      <stop offset="0.7" stop-color="var(--silver-mid)"/>
      <stop offset="0.85" stop-color="var(--silver-light)"/>
      <stop offset="1" stop-color="var(--silver-dark)"/>
    </linearGradient>
    <linearGradient id="crimson" x1="0" y1="0" x2="1" y2="0">
      <stop offset="0" stop-color="var(--crimson-deep)"/>
      <stop offset="0.15" stop-color="var(--crimson)"/>
      <stop offset="0.45" stop-color="var(--crimson-deep)"/>
      <stop offset="0.6" stop-color="var(--crimson)"/>
      <stop offset="0.85" stop-color="var(--crimson)"/>
      <stop offset="1" stop-color="var(--crimson-deep)"/>
    </linearGradient>
    <radialGradient id="ornament-tone" cx="0.5" cy="0.5" r="0.6">
      <stop offset="0" stop-color="#8a8a8a"/>
      <stop offset="0.6" stop-color="#3c3c3c"/>
      <stop offset="1" stop-color="#111111"/>
    </radialGradient>
  </defs>

  <rect class="label-ground" width="1200" height="1000" fill="var(--label-black)"/>
  <rect class="label-frame" x="19" y="19" width="1162" height="962" fill="none" stroke="url(#silver)" stroke-width="16"/>

  <g class="label-type">
    <text class="strength-line" x="184" y="180" fill="url(#silver)" font-size="196"
          textLength="832" lengthAdjust="spacingAndGlyphs">NAVY STRENGTH BRITISH</text>

    <rect class="gin-ornament" x="200" y="240" width="800" height="360" fill="url(#ornament-tone)"
          role="img" aria-label="Ornamental silver GIN lettering entwined with oak leaves and acorns"/>

    <g class="brand-name" transform="translate(68 812) scale(0.42 1)">
      <text fill="url(#crimson)" font-size="200" textLength="2457" lengthAdjust="spacing">COPPER LANTERN</text>
    </g>

    <text class="volume" x="266" y="942" fill="url(#silver)" font-size="110"
          textLength="70" lengthAdjust="spacingAndGlyphs">50<tspan font-size="58">CL</tspan></text>

    <text class="abv" x="804" y="942" fill="url(#silver)" font-size="110"
          textLength="130" lengthAdjust="spacingAndGlyphs">57%<tspan font-size="58">ABV</tspan></text>
  </g>
</svg>
</body>
</html>
```